Velmar Industrial Coatings

We are looking to improve our business cards. Our company installs industrial floor and wall coatings in industrial, chemical and food processing plants.
Our coatings which consist of epoxy, urethane, and vinyl esters provide chemical and abrasion resistant surface with non-skid properties that are easy to clean.

Target Market(s)

food manufacturing, chemical plants, breweries and wineries, warehouses, clean room floors.

Industry/Entity Type

Construction

Contact Information for Business Card

improved current logo.

Colors

Designer to choose colors to be used in the design.

Requirements
Must have
• the information from uploaded file
Nice to have
• "Coatings built for the toughest floors."

```html
<!DOCTYPE html>
<html lang="en">
<head>
<meta charset="utf-8">
<title>Velmar Industrial Coatings – Business Card</title>
<link href="https://fonts.googleapis.com/css2?family=Arimo:wght@400;700&display=swap" rel="stylesheet">
<style>
  :root {
    --page-bg: #e9e7e2;
    --card-white: #fbfbfa;
    --ink: #1c1c1c;
    --text-grey: #3a3a3a;
    --brand-green: #4b6a2a;
    --band-green: #415f24;
    --rule: #7d8f5d;
  }
  * { margin: 0; padding: 0; box-sizing: border-box; }
  html, body {
    width: 1200px; height: 780px; overflow: hidden;
    background: var(--page-bg);
  }
  .canvas {
    width: 1200px; height: 780px;
    display: flex; align-items: center; justify-content: center;
  }
  .card {
    position: relative;
    width: 1000px; height: 572px;
    background: var(--card-white);
    box-shadow: 0 10px 30px rgba(0,0,0,0.18);
    font-family: "Arimo", Arial, sans-serif;
    color: var(--text-grey);
    overflow: hidden;
  }
  .brand-name {
    position: absolute; left: 70px; top: 80px;
    font-family: "Arimo", Arial, sans-serif;
    font-weight: 700; font-size: 44px; line-height: 1;
    color: var(--ink);
  }
  .person {
    position: absolute; left: 520px; top: 200px;
  }
  .person-name {
    font-weight: 700; font-size: 34px; color: var(--brand-green);
    text-transform: uppercase; line-height: 1.05;
  }
  .person-phone { font-size: 22px; margin-top: 4px; color: var(--text-grey); }
  .divider {
    position: absolute; left: 50px; right: 50px; top: 318px;
    height: 1px; background: var(--rule);
  }
  .contact-list {
    position: absolute; left: 60px; top: 336px;
    list-style: none; font-size: 21px; line-height: 29px;
  }
  .contact-list li { display: flex; align-items: center; gap: 12px; }
  .contact-list svg { width: 20px; height: 20px; flex: none; }
  .address {
    position: absolute; right: 60px; top: 336px;
    text-align: right; font-size: 21px; line-height: 29px; font-style: normal;
  }
  .address .web { font-weight: 700; color: var(--brand-green); }
  .address .web span { color: var(--text-grey); font-weight: 400; }
  .tagline-band {
    position: absolute; left: 0; right: 0; bottom: 0; height: 82px;
    background: var(--band-green);
    display: flex; align-items: center; justify-content: center;
  }
  .tagline {
    color: #fff; font-weight: 700; font-size: 25px; letter-spacing: 0.5px;
  }
</style>
</head>
<body>
<main class="canvas">
  <article class="card">
    <h1 class="brand-name">Velmar Industrial Coatings Inc.</h1>

    <section class="person">
      <h2 class="person-name">Reid Calloway</h2>
      <p class="person-phone">1-800-555-0142</p>
    </section>

    <div class="divider"></div>

    <ul class="contact-list">
      <li>
        <svg viewBox="0 0 20 20" aria-label="Phone"><path fill="#4b6a2a" d="M3 7c0-3 3-4 7-4s7 1 7 4v2h-4V7H7v2H3z M5 10h10l2 7H3z"/><circle cx="10" cy="13.5" r="2" fill="#fbfbfa"/></svg>
        (360) 555-0131
      </li>
      <li>
        <svg viewBox="0 0 20 20" aria-label="Fax"><rect x="5" y="2" width="10" height="6" fill="#4b6a2a"/><rect x="2" y="8" width="16" height="8" fill="#4b6a2a"/><rect x="5" y="13" width="10" height="5" fill="#fbfbfa" stroke="#4b6a2a" stroke-width="1.5"/></svg>
        (360) 555-0133
      </li>
      <li>
        <svg viewBox="0 0 20 20" aria-label="Mobile"><rect x="3" y="3" width="14" height="14" fill="none" stroke="#4b6a2a" stroke-width="2"/></svg>
        (360) 555-0176
      </li>
      <li>
        <svg viewBox="0 0 20 20" aria-label="Email"><rect x="2" y="4" width="16" height="12" fill="#4b6a2a"/><path d="M2 4l8 7 8-7" fill="none" stroke="#fbfbfa" stroke-width="1.5"/></svg>
        reid@velmarfloors.com
      </li>
    </ul>

    <address class="address">
      Velmar Inc.<br>
      PO Box 412<br>
      Fernbrook, WA 98500<br>
      <span class="web"><span>www.</span>velmarfloors<span>.com</span></span>
    </address>

    <footer class="tagline-band">
      <p class="tagline">Coatings built for the toughest floors.</p>
    </footer>
  </article>
</main>
</body>
</html>
```